Conservative, Modern and Sharp Builder Business card

Hi there,
We would like to update our existing business card.
I have attached photos of existing business card, logo and van sign.

I would like the business card to also list what we do :
Renovation • New Build • Alteration
Extension • Bathroom • Maintenance.(Seperated by dots)

Contact number : 021 0483 0752
(With that exact spacing)

Ideally when people looking from about 2-3 metres, they know that it is a builder’s business card

Open to suggestions on fonts, layout, style of business card

PLEASE ONLY SUBMIT YOUR BEST OR MAX 3 DESIGNS FOR EACH DESIGNER

Thanks

Construction. Renovation

Details should be the same as the existing card. And addition of what we do.

• The new business card must not have the same layout as our existing one. Thanks

```html
<!DOCTYPE html>
<html lang="en">
<head>
<meta charset="utf-8">
<title>KestrelBuild Business Card</title>
<link href="https://fonts.googleapis.com/css2?family=Roboto:wght@400;700&display=swap" rel="stylesheet">
<style>
  :root {
    --page: #ececec;
    --card-dark: #1f1f1f;
    --card-light: #f4f4f4;
    --ink-dark: #2b2b2b;
    --ink-silver: #b9b9bb;
    --band-name: #3d3d3d;
    --band-contact: #58585a;
    --band-text: #f2f2f2;
  }
  * { box-sizing: border-box; margin: 0; padding: 0; }
  html, body { width: 1200px; height: 900px; overflow: hidden; }
  body {
    background: var(--page);
    font-family: "Roboto", Arial, sans-serif;
    display: flex;
    flex-direction: column;
    align-items: center;
    justify-content: center;
    gap: 40px;
  }
  .card {
    width: 630px;
    height: 360px;
    position: relative;
    box-shadow: 0 6px 18px rgba(0,0,0,0.18);
  }

  /* Front */
  .card-front {
    background: var(--card-dark);
    color: var(--ink-silver);
    display: flex;
    flex-direction: column;
    align-items: center;
    padding-top: 78px;
  }
  .brand {
    display: flex;
    align-items: center;
    gap: 14px;
    font-weight: 700;
    letter-spacing: 0.5px;
  }
  .brand-mark { width: 30px; height: 30px; background: currentColor; }
  .card-front .brand { font-size: 52px; }
  .services { text-align: center; line-height: 1.3; }
  .card-front .services { font-size: 21px; margin-top: 22px; }
  .rule {
    width: 500px;
    height: 2px;
    background: var(--ink-silver);
    margin-top: 30px;
  }

  /* Back */
  .card-back {
    background: var(--card-light);
    color: var(--ink-dark);
  }
  .back-brand {
    position: absolute;
    left: 0; right: 0; top: 48px;
    display: flex;
    flex-direction: column;
    align-items: center;
  }
  .card-back .brand { font-size: 40px; }
  .brand-mark.small { width: 22px; height: 22px; }
  .card-back .services { font-size: 14px; margin-top: 10px; }
  .band {
    position: absolute;
    left: 0; right: 0;
    top: 200px;
    height: 110px;
    display: flex;
    color: var(--band-text);
  }
  .band-name {
    width: 52%;
    background: var(--band-name);
    display: flex;
    flex-direction: column;
    justify-content: center;
    padding-left: 40px;
  }
  .person { font-size: 30px; }
  .role { font-size: 18px; margin-top: 2px; }
  .band-contact {
    flex: 1;
    background: var(--band-contact);
    display: flex;
    flex-direction: column;
    justify-content: center;
    gap: 3px;
    padding-left: 26px;
    font-size: 16px;
  }
  .contact-line { display: flex; align-items: center; gap: 10px; }
  .contact-line svg { width: 13px; height: 13px; flex: none; }
</style>
</head>
<body>
  <section class="card card-front">
    <div class="brand"><span class="brand-mark"></span>KestrelBuild</div>
    <p class="services">Renovation • New Build • Alteration<br>Extension • Bathroom • Maintenance.</p>
    <div class="rule"></div>
  </section>

  <section class="card card-back">
    <div class="back-brand">
      <div class="brand"><span class="brand-mark small"></span>KestrelBuild</div>
      <p class="services">Renovation • New Build • Alteration<br>Extension • Bathroom • Maintenance.</p>
    </div>
    <div class="band">
      <div class="band-name">
        <p class="person">Tomas Varga</p>
        <p class="role">Residential Builder</p>
      </div>
      <div class="band-contact">
        <p class="contact-line">
          <svg viewBox="0 0 16 16" aria-hidden="true"><path d="M3 1l3 3-2 2c1 2 3 4 5 5l2-2 3 3-2 3C6 15 1 10 0 3z" fill="currentColor"/></svg>
          021 0483 0752
        </p>
        <p class="contact-line">
          <svg viewBox="0 0 16 16" aria-hidden="true"><rect x="1" y="3" width="14" height="10" fill="none" stroke="currentColor" stroke-width="1.5"/><path d="M1 3l7 6 7-6" fill="none" stroke="currentColor" stroke-width="1.5"/></svg>
          hello@kestrelbuild.nz
        </p>
        <p class="contact-line">
          <svg viewBox="0 0 16 16" aria-hidden="true"><circle cx="8" cy="8" r="6.5" fill="none" stroke="currentColor" stroke-width="1.5"/><path d="M1.5 8h13M8 1.5c3 3 3 10 0 13M8 1.5c-3 3-3 10 0 13" fill="none" stroke="currentColor" stroke-width="1.2"/></svg>
          www.kestrelbuild.nz
        </p>
        <p class="contact-line">
          <svg viewBox="0 0 16 16" aria-hidden="true"><circle cx="8" cy="8" r="6.5" fill="none" stroke="currentColor" stroke-width="1.5"/></svg>
          KestrelBuild.nz
        </p>
      </div>
    </div>
  </section>
</body>
</html>
```